Bed Company needs business card

Hello, we are a bed company that makes specialized magnets for beds. We are an alternative healing company. I need a modern and upscale business card. Please incorporate my logo for the card.

Accepted file formats are AI, EPS, and Press-Ready PDFS.

Please include all fonts or convert them to outlines regardless of file type.

If you are designing the card in Photoshop the file Must be 1200dpi.

I am open to anything for the business card.  I really like all of your designs and if you want to change the color of the logo, you can.  I will be making the final selection by Friday.  Thank You for all of your designs.  Feel Free to submit different color logos if you want.  

Reason: I will make a decision Final on Friday April 20th. 2012. Good Luck and Thank you all for the designs.

Target Market(s)

My target Market is people, who are looking for alternative healing.

Industry/Entity Type

Business

Requirements
Must have
• My logo must be incorporated. The front card must have

Name
Job Title

Address
Work
Cell
Fax
email
web

Just put in fake info for the card.

The back of the card. I want the logo on the back with color. I just want it to look modern and cool.

```html
<!DOCTYPE html>
<html lang="en">
<head>
<meta charset="utf-8">
<title>Lodestone Rest — Business Card</title>
<link href="https://fonts.googleapis.com/css2?family=Open+Sans:wght@400;600;700;800&display=swap" rel="stylesheet">
<style>
  :root {
    --green-dark: #3b6a3d;
    --green-light: #6cbf48;
    --ink: #1f1f1f;
    --ink-soft: #555555;
    --paper: #ffffff;
    --backdrop: #f1f2ef;
  }
  * { margin: 0; padding: 0; box-sizing: border-box; }
  html, body {
    width: 1200px; height: 900px; overflow: hidden;
    background: var(--backdrop);
    font-family: "Open Sans", Arial, sans-serif;
  }
  .canvas { position: relative; width: 1200px; height: 900px; }
  .card {
    position: absolute; width: 560px; height: 320px;
    background: var(--paper); overflow: hidden;
    box-shadow: 0 10px 28px rgba(0,0,0,0.16);
  }
  /* back side */
  .card-back { left: 60px; top: 110px; }
  .brand { position: absolute; left: 46px; top: 54px; display: flex; align-items: center; gap: 16px; }
  .brand-square { width: 44px; height: 44px; background: var(--green-dark); }
  .brand-name { font-size: 50px; font-weight: 800; color: var(--green-dark); letter-spacing: -0.5px; line-height: 1; }
  .tagline {
    position: absolute; right: 40px; top: 124px;
    font-size: 21px; font-weight: 400; letter-spacing: 2px; color: var(--green-dark);
  }
  .back-band { position: absolute; left: 0; bottom: 0; width: 560px; height: 130px; }
  .back-web {
    position: absolute; left: 0; right: 0; bottom: 34px; text-align: center;
    font-size: 24px; font-weight: 700; color: var(--paper); letter-spacing: 0.5px;
  }
  /* front side */
  .card-front { left: 580px; top: 470px; }
  .front-block { position: absolute; left: 0; top: 0; width: 220px; height: 320px; }
  .holder { position: absolute; right: 30px; top: 26px; text-align: right; }
  .holder-name { font-size: 15px; font-weight: 700; color: var(--ink); }
  .holder-title { font-size: 12px; font-weight: 400; color: var(--ink-soft); }
  .contact {
    position: absolute; left: 250px; top: 130px; list-style: none;
    font-size: 16px; font-weight: 600; color: var(--ink); line-height: 1.45;
  }
</style>
</head>
<body>
<main class="canvas">

  <section class="card card-back" aria-label="Card back">
    <div class="brand">
      <span class="brand-square"></span>
      <span class="brand-name">Lodestone Rest</span>
    </div>
    <p class="tagline">Alternative Healing</p>
    <svg class="back-band" viewBox="0 0 560 130" aria-hidden="true">
      <path d="M0 40 Q280 -20 560 60 L560 130 L0 130 Z" fill="var(--green-dark)"/>
    </svg>
    <p class="back-web">www.lodestonerest.com</p>
  </section>

  <section class="card card-front" aria-label="Card front">
    <svg class="front-block" viewBox="0 0 220 320" aria-hidden="true">
      <path d="M0 0 L170 0 L200 320 L0 320 Z" fill="var(--green-dark)"/>
      <path d="M176 0 L184 0 L214 320 L206 320 Z" fill="var(--green-light)"/>
    </svg>
    <div class="holder">
      <p class="holder-name">Clara Dunn</p>
      <p class="holder-title">Sales Representative</p>
    </div>
    <ul class="contact">
      <li>218 North Ember Lane</li>
      <li>W: 555.240.1187</li>
      <li>C: 555.318.4402</li>
      <li>F: 555.672.9035</li>
      <li>clara@lodestonerest.com</li>
      <li>www.lodestonerest.com</li>
    </ul>
  </section>

</main>
</body>
</html>
```